Postcard Design

I need a two-sided promotional postcard designed to address the key business areas of my gluten free wellness retreat.

Please Note: The "mailer" template is not required for the reverse as these postcards are for event handouts only. Please use the attached "front" template for each side (both front and back)

Possibly, services on one side and photos/visuals on the other side with contact information on either or both sides.

www.hollowpinekitchen.net is my website.

Key business areas:

STAY: Retreat stays + associated care program
PLAY: Bed and Breakfast
LEARN: Individual Health Coaching
GROW: Community classes / events / cooking classes

Retreat Stay Client: Female, 40+. Expendable income, but she likely has a very busy career and family so she does not have the time to spend this on herself. Her wellness takes a backseat to her career and family life. She often remembers being “thinner when she was younger” and has a lot of preconceived notions about dieting. She is open to alternative healthcare options, and thinks she does a pretty good job keeping up with them via Dr. Vel, and magazine articles etc. She needs a compassionate, non-intimidating care provider who she trusts will not “judge” her.

Coaching Client: Male + Female, from mid-40s to retirement age and older. They likely also have some amount of expendable income, and are not necessarily bound my medical or other insurance in terms of seeking alternative treatment. In their earlier adult years they were likely active and well-traveled. They have some adult children who are also quite successful, and so in their golden years, they are comfortable to spend money on themselves rather than assist adult children/grandkids. Frankly, they can somewhat skeptical of alternative wellness providers. They likely suffer from a myriad of age related maladies, and need a compassionate standard of care.

Visual Identity:

 Color/visual TO DO:
o Align color palate with warmth of the desert / desert scenery – without being to “Western”
o Incorporate sky blues, and tones found in flowers
o Feature vegetal, floral, or similar imagery (preferably that of the actual retreat location and surrounding
area)

 Color /visual DO NOT DO:
o Overly bright, pop color tones
o Sharp, bright tones
o Overtly “stock” photos – note: you can use these, but try to steer clear of obviously fake photos.

Industry/Entity Type

Healthcare

Requirements
Must have
• Must list services offers
Must use real photos of retreat and/or cooking shots
Must use at least one photo of the pool

Must have email, website and phone number

I do not want the mail ready set up. These postcards are for event handouts only.

I would like different information on each side of the postcard. Possibly, services on one side and photos/visuals on the other side with contact information on either or both sides. I attached an example of previous printed materials as well as my website to get a feel for my business.

Additionally, once this project is done, I would like to work with the designer for other elements? I'm looking for a matching business card and tri-fold brochure.

```html
<!DOCTYPE html>
<html lang="en">
<head>
<meta charset="utf-8">
<title>Hollow Pine Kitchen – Postcard</title>
<link rel="stylesheet" href="https://fonts.googleapis.com/css2?family=Jost:wght@300;400;500;600&display=swap">
<style>
  :root {
    --backdrop: #4d4d4f;
    --card: #ffffff;
    --panel: #d3d1c5;
    --crimson: #c41e47;
    --magenta: #b8378c;
    --ink: #1d1d1d;
    --band: #a9c47f;
    --rule: #ffffff;
  }
  * { box-sizing: border-box; margin: 0; padding: 0; }
  html, body { width: 1200px; height: 958px; overflow: hidden; }
  body { background: var(--backdrop); font-family: "Jost", "Futura", sans-serif; color: var(--ink); position: relative; }

  .postcard { position: absolute; left: 79px; top: 78px; width: 1046px; height: 804px; background: var(--card); }

  .services { position: absolute; left: 22px; top: 15px; width: 694px; height: 307px; background: var(--panel); padding: 24px 26px 0 27px; }
  .services__headline { color: var(--crimson); font-weight: 500; font-size: 35px; line-height: 42px; letter-spacing: 0.2px; }
  .services__list { list-style: none; margin-top: 12px; width: 642px; }
  .services__item { position: relative; font-size: 24px; line-height: 45px; height: 48px; padding-left: 26px; border-bottom: 2px solid var(--rule); font-weight: 400; }
  .services__item:last-child { border-bottom: none; }
  .services__item::before { content: ""; position: absolute; left: 2px; top: 17px; width: 11px; height: 11px; background: var(--crimson); }
  .services__key { font-weight: 600; }

  .photo { position: absolute; left: 741px; width: 284px; }
  .photo--sunset { top: 15px; height: 307px; background: linear-gradient(200deg, #f7d98a 0%, #d9913f 22%, #7a5434 50%, #3b2e26 78%, #2a2724 100%); }
  .photo--market { top: 510px; height: 218px; background: linear-gradient(180deg, #d9dfcf 0%, #7d9a58 40%, #3f6a2e 75%, #2f4b25 100%); }

  .badge { position: absolute; left: 741px; top: 340px; width: 284px; height: 150px; background: var(--crimson); color: #fff; text-align: center; }
  .badge__figure { font-weight: 300; font-size: 62px; line-height: 62px; margin-top: 10px; letter-spacing: 1px; }
  .badge__label { font-weight: 300; font-size: 24px; line-height: 25px; margin-top: 8px; }

  .persona__tag { position: absolute; left: 25px; width: 251px; height: 30px; background: var(--magenta); color: #fff; font-size: 19px; font-weight: 500; line-height: 30px; padding-left: 15px; letter-spacing: 0.3px; }
  .persona__text { position: absolute; left: 27px; width: 670px; font-size: 18.4px; line-height: 25.5px; font-weight: 400; }
  .persona--retreat .persona__tag { top: 355px; }
  .persona--retreat .persona__text { top: 392px; }
  .persona--coaching .persona__tag { top: 544px; }
  .persona--coaching .persona__text { top: 587px; }

  .contact { position: absolute; left: 22px; top: 743px; width: 1005px; height: 43px; background: var(--band); display: flex; align-items: center; justify-content: center; font-size: 21px; gap: 26px; }
</style>
</head>
<body>
  <article class="postcard">
    <section class="services">
      <h1 class="services__headline">Small changes made consistently<br>over time produce big results</h1>
      <ul class="services__list">
        <li class="services__item"><span class="services__key">STAY:</span> Retreat stays + associated care program</li>
        <li class="services__item"><span class="services__key">PLAY:</span> Bed and Breakfast</li>
        <li class="services__item"><span class="services__key">LEARN:</span> Individual Health Coaching</li>
        <li class="services__item"><span class="services__key">GROW:</span> Community classes / events / cooking classes</li>
      </ul>
    </section>

    <div class="photo photo--sunset" role="img" aria-label="Desert road at sunset with palm trees and mountains"></div>

    <div class="badge">
      <p class="badge__figure">100%</p>
      <p class="badge__label">GLUTEN-FREE<br>ENVIRONMENT</p>
    </div>

    <div class="photo photo--market" role="img" aria-label="Retreat host holding fresh kale at a farmers market stand"></div>

    <section class="persona persona--retreat">
      <h2 class="persona__tag">RETREAT STAY CLIENT</h2>
      <p class="persona__text">Female, 40+. Expendable income, but she likely has a very busy career and family so she does not have the time to spend this on herself. Her wellness takes a backseat to her career and family life. She often remembers being “thinner when she was younger” and has a lot of preconceived notions about dieting.</p>
    </section>

    <section class="persona persona--coaching">
      <h2 class="persona__tag">COACHING CLIENT</h2>
      <p class="persona__text">Coaching Client: Male + Female, from mid-40s to retirement age and older. They likely also have some amount of expendable income, and are not necessarily bound my medical or other insurance in terms of seeking alternative treatment. In their earlier adult years they were likely active and well-traveled.</p>
    </section>

    <footer class="contact">
      <span>T: 213.555.0147</span><span>|</span>
      <span>W: hollowpinekitchen.net</span><span>|</span>
      <span>E: hello@hollowpinekitchen.net</span>
    </footer>
  </article>
</body>
</html>
```